Bref créative
Website template for salsa company
Abuela Rufina's Roasted Dip
Food
www.RoastedDipco.com
Startup salsa company. We aim to change peoples thinking that salsa is just for "Chips & Salsa". The website will contain recipes and ideas for using the salsa in others ways as well as an ecommerce page where you can buy it.
Dislike dark backgrounds
Like easy navigation
Like dynamic content
Like a little humor in pictures such characters (peppers that smile etc)
Colorful
Humorous
top
www.kendrawpepperjars.com
Rather than just using the 3 "primary" colors in the logo please fell free to use complimentary colors as well as the monochromatic colors for each of the 3.
I will answer any questions you may have.
Company logo
Mild pepper
Hispanic designs
Happy pepper
Mean looking pepper
3 peppers
3 peppers #2
3 peppers #3
flaming peppers
habanero pepper

```html
<!DOCTYPE html>
<html lang="en">
<head>
<meta charset="utf-8">
<title>Abuela Rufina's Roasted Dip</title>
<link href="https://fonts.googleapis.com/css2?family=Arimo:ital,wght@0,400;0,700;1,700&display=swap" rel="stylesheet">
<style>
  :root {
    --ember: #8e1208;
    --flame: #e2491a;
    --sun: #f6a12a;
    --leaf: #2f9a3c;
    --title-green: #2fa64a;
    --nav-black: #121006;
    --nav-gold: #b8892a;
    --highlight: #f4d21c;
    --cream: #fdf3c4;
    --white: #ffffff;
    --chili: #c8180c;
    --jalapeno: #3f8a1e;
  }
  * { margin: 0; padding: 0; box-sizing: border-box; }
  html, body { width: 1200px; height: 961px; overflow: hidden; }
  body {
    position: relative;
    font-family: "Arimo", Arial, sans-serif;
    background: linear-gradient(180deg, var(--ember) 0px, var(--flame) 110px, var(--sun) 200px, var(--leaf) 300px, var(--leaf) 100%);
  }
  .award-badge {
    position: absolute; top: 40px; width: 150px; height: 168px;
    background: var(--white); border: 4px solid var(--chili);
  }
  .award-badge--left { left: 104px; }
  .award-badge--right { left: 946px; }
  .brand-mark {
    position: absolute; left: 420px; top: 40px; width: 360px; height: 120px;
    display: flex; align-items: center; justify-content: center; text-align: center;
    font-weight: 700; font-size: 40px; line-height: 1.1; color: var(--ember);
  }
  .site-title {
    position: absolute; left: 0; width: 1200px; top: 172px; text-align: center;
    font-weight: 700; font-style: italic; font-size: 36px; color: var(--title-green);
  }
  .main-nav {
    position: absolute; left: 104px; top: 234px; width: 992px; height: 60px;
    background: linear-gradient(180deg, #2a2410, var(--nav-black));
    border-top: 3px solid var(--nav-gold); border-bottom: 3px solid var(--nav-gold);
    display: flex; align-items: center; justify-content: space-around; padding: 0 20px;
  }
  .main-nav a { color: var(--cream); text-decoration: none; font-size: 29px; }
  .main-nav a.is-current { color: var(--highlight); }
  .product { position: absolute; width: 330px; height: 140px; }
  .product__art {
    position: absolute; left: 0; top: 0; width: 60px; height: 110px;
    background: linear-gradient(160deg, var(--sun), var(--chili));
    border: 2px solid var(--white);
  }
  .product__art--green { background: linear-gradient(160deg, #9ad04a, var(--jalapeno)); }
  .product__body { position: absolute; left: 68px; top: 0; width: 248px; }
  .product__name { color: var(--highlight); font-weight: 700; font-size: 12px; text-transform: uppercase; }
  .product__text { color: var(--white); font-size: 10.5px; line-height: 1.28; margin-top: 2px; }
  .social { position: absolute; left: 880px; top: 770px; display: flex; gap: 6px; }
  .social span {
    font-size: 11px; font-weight: 700; color: var(--white);
    display: flex; align-items: center; gap: 3px;
  }
  .social span::before { content: ""; width: 12px; height: 12px; background: var(--white); }
  .partners {
    position: absolute; left: 239px; top: 806px; width: 727px; height: 86px;
    background: #1c1a14; border: 4px solid var(--nav-gold);
    display: flex; align-items: center; justify-content: space-around;
  }
  .partners span {
    background: var(--white); color: #1c2a6a; font-weight: 700; font-size: 18px;
    padding: 12px 14px; min-width: 130px; text-align: center;
  }
  .copyright {
    position: absolute; left: 0; width: 1200px; top: 925px; text-align: center;
    font-size: 15px; color: #123;
  }
</style>
</head>
<body>
  <div class="award-badge award-badge--left" role="img" aria-label="Hot sauce award badge"></div>
  <div class="brand-mark">Abuela Rufina's Roasted Dip</div>
  <div class="award-badge award-badge--right" role="img" aria-label="Hot sauce award badge"></div>
  <h1 class="site-title">Abuela Rufina's Roasted Dip Co.</h1>

  <nav class="main-nav">
    <a class="is-current" href="#">Home</a>
    <a href="#">Buy Online</a>
    <a href="#">In Stores</a>
    <a href="#">Recipes</a>
    <a href="#">Testimonials</a>
    <a href="#">About Us</a>
    <a href="#">Contact Us</a>
  </nav>

  <article class="product" style="left:239px; top:312px;">
    <div class="product__art" role="img" aria-label="Smiling orange pepper illustration"></div>
    <div class="product__body">
      <h2 class="product__name">Honey Ember</h2>
      <p class="product__text">A gentle blend of ripe peppers, roasted garlic and a touch of honey. It starts sweet, finishes warm and brings a bright glow to tacos, grilled chicken, eggs and even your morning toast.</p>
    </div>
  </article>

  <article class="product" style="left:660px; top:312px;">
    <div class="product__art" role="img" aria-label="Mean looking red pepper illustration"></div>
    <div class="product__body">
      <h2 class="product__name">Dark Rival</h2>
      <p class="product__text">Built for the brave who want real fire. Smoked chiles and dark spices team up for a slow burn that lingers. Try a spoonful in chili, stews or marinades if you dare.</p>
    </div>
  </article>

  <article class="product" style="left:239px; top:466px;">
    <div class="product__art" role="img" aria-label="Flaming pepper illustration"></div>
    <div class="product__body">
      <h2 class="product__name">Campfire Glow</h2>
      <p class="product__text">Deep smoky chiles meet fire roasted tomato in a rich, bold dip. Stir it into beans, brush it over ribs or spread it on burgers for a campfire flavor any night of the week.</p>
    </div>
  </article>

  <article class="product" style="left:660px; top:466px;">
    <div class="product__art product__art--green" role="img" aria-label="Happy green pepper illustration"></div>
    <div class="product__body">
      <h2 class="product__name">Green Sunrise</h2>
      <p class="product__text">Fresh green peppers with a mellow sweetness that keeps friends coming back. Perfect for dipping, topping nachos or mixing into cream cheese for a quick party spread everyone will love.</p>
    </div>
  </article>

  <article class="product" style="left:239px; top:616px;">
    <div class="product__art" role="img" aria-label="Three peppers illustration"></div>
    <div class="product__body">
      <h2 class="product__name">Berry Blaze</h2>
      <p class="product__text">Berries and peppers share the stage in this summer favorite. Strawberries, blackberries and a hint of chile make it great over ice cream, grilled pork or a simple bowl of yogurt.</p>
    </div>
  </article>

  <article class="product" style="left:660px; top:616px;">
    <div class="product__art" role="img" aria-label="Shouting pepper illustration"></div>
    <div class="product__body">
      <h2 class="product__name">Lime Howler</h2>
      <p class="product__text">A zesty green dip that packs more punch than you expect. Tangy lime and roasted peppers shine on fish tacos, salads and wings. Our tasters called it beyond expectation.</p>
    </div>
  </article>

  <div class="social">
    <span>Sharebox</span>
    <span>Chirpline</span>
    <span>Clipview</span>
  </div>

  <div class="partners">
    <span>Kendraw Jars</span>
    <span>Verdano</span>
    <span>Arcolo Foods</span>
    <span>Savorline</span>
  </div>

  <p class="copyright">Copyright © 2010</p>
</body>
</html>
```